Business Card Design Project

we need a business card design for our company: www.plomvik.ch
It's important to include our already existing logo (see website)

```html
<!DOCTYPE html>
<html lang="en">
<head>
<meta charset="utf-8">
<title>Plomvik – Business Card</title>
<link rel="stylesheet" href="https://fonts.googleapis.com/css2?family=Ubuntu:wght@400;500&family=Open+Sans:wght@400&display=swap">
<style>
  :root {
    --page-top: #ffffff;
    --page-bottom: #dcdcdc;
    --label: #9a9a9a;
    --brand-blue: #1f6fb5;
    --text-blue: #2a78c2;
    --band-light: #7ab7e0;
    --band-blue: #0f6fbf;
    --band-dark: #333333;
    --card-back-deep: #084c92;
    --card-back-mid: #1a70bd;
    --white: #ffffff;
  }
  * { box-sizing: border-box; margin: 0; padding: 0; }
  html, body { width: 1200px; height: 1050px; overflow: hidden; }
  body {
    position: relative;
    background: linear-gradient(180deg, var(--page-top) 0%, var(--page-bottom) 100%);
    font-family: "Ubuntu", sans-serif;
  }
  .side-label {
    position: absolute;
    left: 240px;
    font-family: "Open Sans", sans-serif;
    font-size: 19px;
    letter-spacing: 1px;
    color: var(--label);
  }
  .side-label--front { top: 90px; }
  .side-label--back { top: 555px; }

  .card {
    position: absolute;
    left: 284px;
    width: 636px;
    height: 364px;
    overflow: hidden;
    box-shadow: 0 3px 8px rgba(0,0,0,0.28);
  }
  .card--front {
    top: 150px;
    background: #ffffff;
  }
  .card--back {
    top: 601px;
    background: radial-gradient(ellipse at 40% 55%, var(--card-back-mid) 0%, var(--card-back-deep) 85%);
  }
  .card__texture {
    position: absolute;
    inset: 0;
  }
  .card--front .card__texture {
    background: linear-gradient(120deg, rgba(255,255,255,0) 40%, rgba(228,228,228,0.8) 100%);
  }
  .card--back .card__texture {
    background: linear-gradient(120deg, rgba(255,255,255,0) 45%, rgba(255,255,255,0.08) 100%);
  }

  .card__url {
    position: absolute;
    top: 30px;
    right: 27px;
    font-size: 19px;
    color: var(--text-blue);
  }
  .brand {
    position: absolute;
    left: 50px;
    top: 66px;
    display: flex;
    align-items: center;
    gap: 14px;
  }
  .brand__square {
    width: 40px;
    height: 40px;
    background: var(--brand-blue);
  }
  .brand__name {
    font-size: 64px;
    font-weight: 500;
    line-height: 1;
    color: var(--brand-blue);
  }
  .brand__tagline {
    position: absolute;
    left: 62px;
    top: 141px;
    font-size: 13px;
    letter-spacing: 0.8px;
    color: #555555;
  }
  .contact {
    position: absolute;
    left: 39px;
    top: 215px;
    font-size: 16px;
    line-height: 22.5px;
    letter-spacing: 0.6px;
    color: var(--text-blue);
    font-style: normal;
  }
  .card__band {
    position: absolute;
    bottom: 0;
    height: 37px;
  }
  .card__band--blue {
    left: 0;
    width: 446px;
    background: linear-gradient(90deg, var(--band-light) 0%, var(--band-blue) 70%);
  }
  .card__band--dark {
    left: 462px;
    right: 0;
    background: var(--band-dark);
  }

  .brand--reverse {
    left: 0;
    right: 0;
    top: 145px;
    justify-content: center;
  }
  .brand--reverse .brand__square { background: var(--white); }
  .brand--reverse .brand__name { color: var(--white); font-size: 68px; }
</style>
</head>
<body>
  <div class="side-label side-label--front">FRONT</div>

  <section class="card card--front">
    <div class="card__texture" role="img" aria-label="Faint grey diagonal background pattern"></div>
    <div class="card__url">www.plomvik.ch</div>
    <div class="brand">
      <span class="brand__square"></span>
      <span class="brand__name">Plomvik</span>
    </div>
    <div class="brand__tagline">ENTERPRISE SOFTWARE SOLUTIONS</div>
    <address class="contact">
      40 Harwell Street<br>
      Suite 210<br>
      Brookfield, MI 48000<br>
      248-555-0100
    </address>
    <div class="card__band card__band--blue"></div>
    <div class="card__band card__band--dark"></div>
  </section>

  <div class="side-label side-label--back">BACK</div>

  <section class="card card--back">
    <div class="card__texture" role="img" aria-label="Faint light-blue diagonal background pattern"></div>
    <div class="brand brand--reverse">
      <span class="brand__square"></span>
      <span class="brand__name">Plomvik</span>
    </div>
  </section>
</body>
</html>
```